Business card for acupunctist in Melbourne. Specialises in Fertility, pre and post natal care, pain

I am looking for a business card which is going to catch people eyes. Two sided, one side in a muted colour (keeping it feminine) (pink or yellow???)maybe with a little simple logo or picture, the other side I was thinking white with 3 colours (pink grey and yellow... Had these in mind.
Info on the card
Marla Quenby Acupuncture

Dr Marla Quenby (TCM Acupuncture)
Acupuncture for balancing body and mind.
Fernleaf Wellcraft
14 Corran Lane, Elsworth 3071.
94726150
0438219574
Marlatcm@quenbymail.com

Some other little logo/ designs I have liked are as follows:
http://www.dorisfelkaclinic.com/rates-and-insurance/
http://www.corinnetavish.com/
http://www.rz-needlework.co.uk/

Target Market(s)

professional women, people in pain, active people, people seeking a healthy lifefstyle.

Industry/Entity Type

Business

Font styles to use
Serif
Sans Serif

Colors
eea4c8
fde08a
aaaaaa

Requirements
Must have
• Must be eye catching, but not too loud and busy. Subltle is good. Simple is also good. The logo could be something that represents growth and health and nurturing. Again not too elaborate, very simple.
Thankyou
Should not have
• Electric colours, crazy fonts, Pictures of yin and yang, candles, or bodies.

```html
<!DOCTYPE html>
<html lang="en">
<head>
<meta charset="utf-8">
<title>Marla Quenby Acupuncture – Business Card</title>
<link href="https://fonts.googleapis.com/css2?family=Mukta:wght@300;400;600&display=swap" rel="stylesheet">
<style>
  :root {
    --pink: #eba3c9;
    --pink-deep: #e596bf;
    --yellow: #fde08a;
    --grey: #9a9a9a;
    --grey-dark: #8a8a8a;
    --white: #ffffff;
    --backdrop: #f1ede8;
  }
  * { box-sizing: border-box; margin: 0; padding: 0; }
  html, body {
    width: 1200px; height: 784px; overflow: hidden;
    background: var(--backdrop);
    font-family: "Mukta", "Helvetica Neue", Arial, sans-serif;
  }
  .canvas { position: relative; width: 1200px; height: 784px; }

  .card {
    position: absolute; width: 560px; height: 320px; overflow: hidden;
    box-shadow: 0 6px 18px rgba(0,0,0,.12);
  }

  /* Front */
  .card--front { left: 70px; top: 70px; background: var(--pink); }
  .card--front .halo {
    position: absolute; left: -70px; top: 20px; width: 260px; height: 260px;
    border-radius: 50%; background: rgba(255,255,255,.22);
  }
  .wordmark { position: absolute; display: flex; align-items: center; gap: 12px; }
  .wordmark__dot { width: 34px; height: 34px; border-radius: 50%; flex: none; }
  .wordmark__name { font-weight: 300; line-height: 1; }
  .wordmark__name .line-1 { display: block; font-size: 40px; }
  .wordmark__name .line-2 { display: block; font-size: 17px; letter-spacing: 9px; margin-top: 8px; color: var(--grey-dark); }

  .card--front .wordmark { left: 150px; top: 100px; }
  .card--front .wordmark__dot { background: var(--white); }
  .card--front .wordmark__name .line-1 { color: var(--white); }

  /* Back */
  .card--back { left: 570px; top: 394px; background: var(--white); }
  .card--back .halo {
    position: absolute; left: -60px; top: 40px; width: 220px; height: 220px;
    border-radius: 50%; background: rgba(235,163,201,.14);
  }
  .card--back .swoosh { position: absolute; inset: 0; }
  .card--back .wordmark { left: 88px; top: 62px; }
  .card--back .wordmark__dot { background: var(--pink); }
  .card--back .wordmark__name .line-1 { color: var(--pink-deep); }

  .practitioner {
    position: absolute; right: 250px; top: 242px; text-align: right;
    color: var(--white); font-size: 12.5px; line-height: 1.3; font-weight: 600;
  }
  .practitioner__name { font-size: 15px; }
  .practitioner__name small { font-size: 11.5px; font-weight: 400; }

  .divider {
    position: absolute; left: 322px; top: 176px; width: 1px; height: 70px;
    background: var(--white);
  }
  .contact {
    position: absolute; left: 334px; top: 174px; list-style: none;
    color: var(--white); font-size: 12.5px; line-height: 1.35; font-weight: 400;
  }
  .contact li { display: flex; align-items: flex-start; gap: 6px; }
  .contact svg { width: 12px; height: 12px; margin-top: 2px; flex: none; fill: var(--white); }
  .contact .no-icon { padding-left: 18px; }
</style>
</head>
<body>
<main class="canvas">

  <section class="card card--front" aria-label="Card front">
    <div class="halo"></div>
    <div class="wordmark">
      <span class="wordmark__dot"></span>
      <span class="wordmark__name"><span class="line-1">Marla Quenby</span><span class="line-2">ACUPUNCTURE</span></span>
    </div>
  </section>

  <section class="card card--back" aria-label="Card back">
    <div class="halo"></div>
    <svg class="swoosh" viewBox="0 0 560 320" preserveAspectRatio="none" aria-hidden="true">
      <path d="M0 320 L0 215 C150 215 380 170 520 0 L560 0 L560 320 Z" fill="var(--pink)"/>
      <path d="M420 120 C470 80 500 40 520 0 L540 0 C515 50 480 90 420 120 Z" fill="var(--yellow)"/>
    </svg>
    <div class="wordmark">
      <span class="wordmark__dot"></span>
      <span class="wordmark__name"><span class="line-1">Marla Quenby</span><span class="line-2">ACUPUNCTURE</span></span>
    </div>

    <div class="practitioner">
      <p class="practitioner__name">Dr Marla Quenby <small>(TCM Acupuncture)</small></p>
      <p>Acupuncture for balancing body and mind.</p>
      <p>Fernleaf Wellcraft</p>
    </div>

    <div class="divider"></div>
    <ul class="contact">
      <li><svg viewBox="0 0 24 24"><path d="M6.6 10.8a15 15 0 006.6 6.6l2.2-2.2c.3-.3.7-.4 1-.2 1.1.4 2.3.6 3.6.6.6 0 1 .4 1 1V20c0 .6-.4 1-1 1A17 17 0 013 4c0-.6.4-1 1-1h3.5c.6 0 1 .4 1 1 0 1.3.2 2.5.6 3.6.1.3 0 .7-.2 1z"/></svg>0438219574</li>
      <li><svg viewBox="0 0 24 24"><path d="M2 5h20v14H2zM4 7v.5l8 5 8-5V7l-8 5z"/></svg>Marlatcm@quenbymail.com</li>
      <li><svg viewBox="0 0 24 24"><path d="M12 3l10 9h-3v9h-5v-6h-4v6H5v-9H2z"/></svg>14 Corran Lane, Elsworth 3071.</li>
      <li class="no-icon">94726150</li>
    </ul>
  </section>

</main>
</body>
</html>
```